Flyer Design Project

I need a flyer designed for my new dog grooming business.
I have just ordered fridge magnet business cards and would like a flyer to send them out with, if you could create a flyer and put some ideas together using the information provided to help promote my business.
The business is called Tallowby Pawcare,
I groom small dogs.
I’d like to have on the flyer the services I offer,
One on one quality care for the customers pet,
Full dog grooms, clipper clips, scissor snips and full shaves,
Sanitary clips, nails clipped, DE shedding,
Various brushing styles and techniques,
All professional equipment and products used,
Medicated shampoos & groomers fluffana wash & colognes,
Hydro dog bath and heater blow dryer.
My profession also id like to have on the flyer:
(A certified pet hygienist & dog Groomer)
I’d like the Tallowby Pawcare logo with the purple paw prints in the writing on the flyer ( will upload pic of logo)
I’d also like the website displayed the email and the phone number all clearly on the flyer also thank you.
Website address: tallowbypawcare.com.au
Email address: info@tallowbypawcare.com.au
Phone number: 0412 580 264
When this flyer has finally been created & finalised, I will need to have sent to me all raw formats and fonts i.e. vector files to be able to provide my sign writer to make the grey in my logo foil instead of silver. Thankyou

regarding size of the flyer i would like the flyer to be size A5 (210mm x 148mm) thankyou.

also when adding dogs to the flyer try sick to the smaller breeds all the flyers look great so far

can i also please have the website,phone number and email writting big or bold on the flyer to stand out.
thankyou
Updates

the text medicated shampoos, groomers fluffana was & colones are now to be changed to

(medicated shampoo's, groomers fluffana & scented colones)

and one on one quality care for the customers pet changed to

(one on one quality care for your pet)

Target Market(s)

dog owners

Industry/Entity Type

Pet

Requirements
Should not have
• no pricings included or any special deals

```html
<!DOCTYPE html>
<html lang="en">
<head>
<meta charset="utf-8">
<title>Tallowby Pawcare – Dog Grooming Flyer</title>
<link rel="stylesheet" href="https://fonts.googleapis.com/css2?family=Open+Sans:wght@400;600;700&display=swap">
<style>
  :root {
    --black: #050505;
    --white: #ffffff;
    --magenta: #e3199b;
    --cyan: #2aa9e3;
    --tan: #c2a487;
    --tan-line: #8c7058;
    --ink: #1c140e;
    --photo-lab: #b89d78;
    --photo-pug: #d8c6ad;
    --photo-shep: #a7784b;
  }
  * { margin: 0; padding: 0; box-sizing: border-box; }
  html, body { width: 1200px; height: 840px; overflow: hidden; background: var(--white); }
  body { font-family: "Open Sans", Arial, sans-serif; }
  .flyer { position: relative; width: 1200px; height: 840px; background: var(--white); }

  .header { position: absolute; left: 0; top: 0; width: 1200px; height: 142px; background: var(--black); }
  .brand { position: absolute; left: 24px; top: 46px; display: flex; align-items: center; gap: 14px; }
  .brand-dot { width: 26px; height: 26px; border-radius: 50%; background: var(--magenta); }
  .brand-name { color: var(--white); font-weight: 700; font-size: 42px; letter-spacing: 0.5px; }
  .contact { position: absolute; right: 34px; text-align: right; color: var(--magenta); font-weight: 400; }
  .contact-phone { top: 12px; font-size: 38px; }
  .contact-email { top: 76px; font-size: 29px; }

  .photos { position: absolute; left: 0; top: 142px; width: 1200px; height: 386px; }
  .photo { position: absolute; border-radius: 40px 40px 6px 6px; }
  .photo-labradors { left: 52px; top: 50px; width: 345px; height: 310px; background: linear-gradient(90deg, #2a2622 0%, #2a2622 45%, var(--photo-lab) 55%, var(--photo-lab) 100%); }
  .photo-pug { left: 496px; top: 62px; width: 240px; height: 298px; background: var(--photo-pug); }
  .photo-shepherds { left: 760px; top: 44px; width: 424px; height: 300px; background: linear-gradient(180deg, #6b4d31 0%, var(--photo-shep) 55%, #c4955f 100%); }

  .services { position: absolute; left: 0; top: 528px; width: 1200px; height: 240px; background: var(--tan); }
  .service-col { position: absolute; top: 58px; }
  .service-col ul { list-style: none; position: absolute; top: 0; }
  .service-col li { font-size: 20px; line-height: 29px; color: var(--ink); white-space: nowrap; }
  .paw { position: absolute; top: 30px; width: 54px; height: 54px; }
  .col-1 { left: 90px; } .col-1 ul { left: 69px; }
  .col-2 { left: 446px; } .col-2 ul { left: 74px; }
  .col-3 { left: 805px; } .col-3 ul { left: 74px; }
  .divider { position: absolute; top: 40px; width: 3px; height: 150px; background: linear-gradient(180deg, transparent, var(--tan-line) 20%, var(--tan-line) 80%, transparent); }
  .divider-1 { left: 382px; } .divider-2 { left: 784px; }

  .footer { position: absolute; left: 0; top: 768px; width: 1200px; height: 72px; background: var(--black); color: var(--cyan); font-size: 23px; }
  .footer-profession { position: absolute; left: 33px; top: 20px; }
  .footer-web { position: absolute; right: 30px; top: 20px; }
</style>
</head>
<body>
<main class="flyer">
  <header class="header">
    <div class="brand">
      <span class="brand-dot"></span>
      <span class="brand-name">Tallowby Pawcare</span>
    </div>
    <div class="contact contact-phone">0412 580 264</div>
    <div class="contact contact-email">info@tallowbypawcare.com.au</div>
  </header>

  <section class="photos">
    <div class="photo photo-labradors" role="img" aria-label="Photo of a black and a yellow labrador puppy sitting together"></div>
    <div class="photo photo-pug" role="img" aria-label="Photo of a fawn pug puppy sitting"></div>
    <div class="photo photo-shepherds" role="img" aria-label="Photo of two shepherd puppies lying side by side"></div>
  </section>

  <section class="services">
    <div class="service-col col-1">
      <svg class="paw" viewBox="0 0 54 54" aria-hidden="true" style="left:-12px"><g fill="#111"><ellipse cx="27" cy="36" rx="13" ry="11"/><ellipse cx="10" cy="22" rx="5.5" ry="7"/><ellipse cx="20" cy="12" rx="5.5" ry="7.5"/><ellipse cx="34" cy="12" rx="5.5" ry="7.5"/><ellipse cx="44" cy="22" rx="5.5" ry="7"/></g></svg>
      <ul><li>Full dog grooms</li><li>clipper clips</li><li>scissor snips</li><li>full shaves</li></ul>
    </div>
    <div class="divider divider-1"></div>
    <div class="service-col col-2">
      <svg class="paw" viewBox="0 0 54 54" aria-hidden="true" style="left:0"><g fill="#111"><ellipse cx="27" cy="36" rx="13" ry="11"/><ellipse cx="10" cy="22" rx="5.5" ry="7"/><ellipse cx="20" cy="12" rx="5.5" ry="7.5"/><ellipse cx="34" cy="12" rx="5.5" ry="7.5"/><ellipse cx="44" cy="22" rx="5.5" ry="7"/></g></svg>
      <ul><li>Sanitary clips</li><li>nails clipped</li><li>DE shedding</li><li>Various brushing styles</li></ul>
    </div>
    <div class="divider divider-2"></div>
    <div class="service-col col-3">
      <svg class="paw" viewBox="0 0 54 54" aria-hidden="true" style="left:0"><g fill="#111"><ellipse cx="27" cy="36" rx="13" ry="11"/><ellipse cx="10" cy="22" rx="5.5" ry="7"/><ellipse cx="20" cy="12" rx="5.5" ry="7.5"/><ellipse cx="34" cy="12" rx="5.5" ry="7.5"/><ellipse cx="44" cy="22" rx="5.5" ry="7"/></g></svg>
      <ul><li>Medicated shampoos</li><li>groomers - fluffana wash</li><li>Hydro dog bath</li><li>heater blow dryer</li></ul>
    </div>
  </section>

  <footer class="footer">
    <span class="footer-profession">A certified pet hygienist &amp; dog Groomer</span>
    <span class="footer-web">www.tallowbypawcare.com.au</span>
  </footer>
</main>
</body>
</html>
```